Pelmoro Travel

We are new traveling company from Italy and looking for a really unique design as soon as possible of the main page.
Travel is an online business. We all do online research before taking a vacation. Since some of us will spend hours researching a trip before finally booking it on a travel website, design is critical.
People looking to travel are going to start with an idea. Some may be browsing for a specific type of trip (river cruise, kayaking, etc.) while others may be looking at specific dates (i.e. February). Still others are considering going to a specific destination such as the Grand Canyon, but all of these visitors are goal-oriented. This type of visitor is frustrated by not finding thle right information easily. This is why travel web design must offer several ways to navigate such as by date, location, activity, cost, etc.
The design should be easy to use for visitors, look fantastic and be easy to update and maintain.
Uploaded some sample pictures but feel free to use your own if it looks good. About colors, blue and white would mix great.

Our future address will be pelmorotravel.com

```html
<!DOCTYPE html>
<html lang="en">
<head>
<meta charset="utf-8">
<title>Pelmoro Travel</title>
<link href="https://fonts.googleapis.com/css2?family=Open+Sans:ital,wght@0,400;0,600;1,400&family=Arimo:wght@400;700&display=swap" rel="stylesheet">
<style>
:root{
  --blue:#1e8fe0;
  --blue-deep:#2f63ad;
  --ink:#222;
  --page:#f3f3f3;
  --white:#fff;
  --dark:#2e2e2e;
  --darker:#151515;
  --hero-top:#6aaee6;
  --hero-bottom:#4fbfd6;
  --thumb:#4ba8cf;
}
*{box-sizing:border-box;margin:0;padding:0}
html,body{width:814px;height:1200px;overflow:hidden}
body{position:relative;background:var(--white);font-family:"Open Sans",sans-serif;color:var(--ink)}
.abs{position:absolute}

.site-header{left:0;top:0;width:814px;height:62px;background:var(--white)}
.brand{left:114px;top:20px;font-size:19px;color:var(--blue);font-weight:400}
.call{right:117px;top:22px;font-size:16px;color:var(--ink)}
.call span{color:var(--blue)}

.main-nav{left:0;top:62px;width:814px;height:43px;background:linear-gradient(#8fd0fa,#47a9ec)}
.main-nav a{position:absolute;top:10px;height:24px;line-height:24px;font-size:11px;color:var(--white);text-decoration:none}
.main-nav a.active{background:var(--white);color:var(--ink);padding:0 9px;border-radius:2px}

.hero{left:0;top:105px;width:814px;height:451px;background:linear-gradient(180deg,var(--hero-top),var(--hero-bottom))}
.hero-title{left:0;top:203px;width:814px;text-align:center;font-size:24px;color:#111;font-weight:400}
.welcome{left:293px;top:264px;width:215px;height:57px;background:var(--blue-deep);color:var(--white);font-size:31px;text-align:center;line-height:57px}
.slider{left:338px;top:418px;width:125px;height:19px;background:rgba(255,255,255,.9);border:1px solid #bbb;border-radius:3px}

.search-band{left:0;top:556px;width:814px;height:64px;background:linear-gradient(#fafbfc,#dde1e6)}
.search-input{left:114px;top:18px;width:267px;height:32px;background:#f1f1f1;border:1px solid #c9c9c9;border-radius:3px 0 0 3px;font-family:Arimo,sans-serif;font-size:12px;color:#555;padding:9px 12px}
.go{left:380px;top:18px;width:41px;height:32px;background:linear-gradient(#4fb0f0,#1c87dc);color:var(--white);font-family:Arimo,sans-serif;font-weight:700;font-size:12px;text-align:center;line-height:32px;border-radius:0 3px 3px 0}
.tagline{left:438px;top:24px;font-family:Arimo,sans-serif;font-size:12px;color:var(--ink)}

.content{left:0;top:620px;width:814px;height:318px;background:var(--page)}
.section-title{font-size:14px;color:var(--ink);font-weight:400}
.offer-card{left:114px;width:342px;height:70px;background:var(--white);border:1px solid #dcdcdc}
.offer-photo{left:0;top:0;width:114px;height:68px;background:var(--thumb)}
.offer-name{left:126px;top:7px;font-size:13px;color:var(--blue)}
.offer-meta{left:126px;top:34px;font-size:9px;line-height:16px;color:var(--ink)}
.more{left:276px;top:28px;width:56px;height:20px;background:linear-gradient(#51b3f2,#1f8ae0);color:var(--white);font-size:11px;text-align:center;line-height:20px;border-radius:3px}

.booking{left:464px;top:662px;width:234px;height:238px;background:linear-gradient(#86cdf8,#2b95e4)}
.booking label{position:absolute;font-family:Arimo,sans-serif;font-size:9px;color:var(--white)}
.field{position:absolute;background:var(--white);border:1px solid #9fd2f5}
.more-options{left:22px;top:204px;font-family:Arimo,sans-serif;font-size:10px;color:var(--white);text-decoration:underline}
.book-search{left:151px;top:195px;width:60px;height:22px;background:linear-gradient(#444,#161616);color:var(--white);font-family:Arimo,sans-serif;font-size:11px;text-align:center;line-height:22px;border-radius:3px}

.reviews{left:0;top:938px;width:814px;height:155px;background:var(--white)}
.next{left:682px;top:9px}
.avatar{left:137px;top:48px;width:78px;height:78px;border-radius:50%;background:#c9c2bc}
.quote{left:266px;top:60px;font-size:9.6px;line-height:14.4px;color:var(--ink);white-space:nowrap}
.author{left:266px;top:104px;font-size:9.6px;line-height:14px;font-style:italic;color:var(--blue)}

.site-footer{left:0;top:1093px;width:814px;height:107px;background:linear-gradient(var(--dark),var(--darker))}
.footer-links{left:0;top:20px;width:814px;text-align:center;font-family:Arimo,sans-serif;font-size:8px;color:var(--white)}
.copyright{left:122px;top:64px;font-family:Arimo,sans-serif;font-size:7px;color:#ddd}
.newsletter{left:554px;top:59px;width:140px;height:16px;background:var(--white);font-family:Arimo,sans-serif;font-size:7px;color:#666;padding:4px 5px}
</style>
</head>
<body>
<header class="site-header abs">
  <div class="brand abs">Pelmoro Travel</div>
  <div class="call abs">Call us ! <span>555 010 010</span></div>
</header>

<nav class="main-nav abs">
  <a class="active" style="left:116px">HOME</a>
  <a style="left:182px">ABOUTUS</a>
  <a style="left:258px">GALLERY</a>
  <a style="left:329px">OFFER</a>
  <a style="left:387px">CONTACTS</a>
</nav>

<section class="hero abs" role="img" aria-label="Tropical beach with palm trees, turquoise sea and clouds">
  <h1 class="hero-title abs">WE ARE A TRAVEL AGENCY</h1>
  <div class="welcome abs">WELCOME</div>
  <div class="slider abs">
    <svg width="125" height="19" viewBox="0 0 125 19">
      <path d="M15 6 l-3 3.5 3 3.5" stroke="#222" stroke-width="1.6" fill="none"/>
      <path d="M26 6 l3 3.5 -3 3.5" stroke="#666" stroke-width="1.4" fill="none"/>
      <line x1="38" y1="2" x2="38" y2="17" stroke="#ccc"/>
      <g fill="#aaa"><circle cx="47" cy="9.5" r="3"/><circle cx="60" cy="9.5" r="3"/><circle cx="86" cy="9.5" r="3"/><circle cx="99" cy="9.5" r="3"/><circle cx="112" cy="9.5" r="3"/></g>
      <circle cx="73" cy="9.5" r="3.3" fill="#111"/>
    </svg>
  </div>
</section>

<section class="search-band abs">
  <div class="search-input abs">Search</div>
  <div class="go abs">GO</div>
  <div class="tagline abs">We all do online research before taking a vacation</div>
</section>

<main class="content abs">
  <h2 class="section-title abs" style="left:114px;top:16px">OUR OFFER</h2>
  <h2 class="section-title abs" style="left:464px;top:16px">BOOKING ONLINE</h2>
</main>

<article class="offer-card abs" style="top:664px">
  <div class="offer-photo abs" role="img" aria-label="Island resort with palm trees and overwater bungalows"></div>
  <div class="offer-name abs">Hawaii Resort</div>
  <div class="offer-meta abs">Arrive date : 2011.05.11<br>Price : 1200</div>
  <div class="more abs">More</div>
</article>
<article class="offer-card abs" style="top:748px">
  <div class="offer-photo abs" role="img" aria-label="Sandy beach lined with palm trees"></div>
  <div class="offer-name abs">Hawaii Resort</div>
  <div class="offer-meta abs">Arrive date : 2011.05.11<br>Price : 1200</div>
  <div class="more abs">More</div>
</article>
<article class="offer-card abs" style="top:830px">
  <div class="offer-photo abs" role="img" aria-label="Blue bay seen from a green hillside"></div>
  <div class="offer-name abs">Hawaii Resort</div>
  <div class="offer-meta abs">Arrive date : 2011.05.11<br>Price : 1200</div>
  <div class="more abs">More</div>
</article>

<form class="booking abs">
  <label style="left:12px;top:21px">From :</label>
  <label style="left:124px;top:21px">To :</label>
  <div class="field" style="left:12px;top:34px;width:98px;height:21px"></div>
  <div class="field" style="left:124px;top:34px;width:98px;height:21px"></div>
  <label style="left:12px;top:72px">Depart :</label>
  <label style="left:124px;top:72px">Return :</label>
  <div class="field" style="left:12px;top:84px;width:98px;height:22px"></div>
  <div class="field" style="left:124px;top:84px;width:98px;height:22px"></div>
  <label style="left:11px;top:123px">Travellers :</label>
  <label style="left:12px;top:150px">Adult :</label>
  <div class="field" style="left:41px;top:145px;width:30px;height:18px"></div>
  <label style="left:85px;top:150px">Child :</label>
  <div class="field" style="left:114px;top:145px;width:29px;height:18px"></div>
  <label style="left:157px;top:150px">Infant :</label>
  <div class="field" style="left:190px;top:145px;width:32px;height:18px"></div>
  <div class="more-options abs">More Options</div>
  <div class="book-search abs">Search</div>
</form>

<section class="reviews abs">
  <h2 class="section-title abs" style="left:114px;top:11px">COSTOMERS REVIEW</h2>
  <svg class="next abs" width="18" height="18" viewBox="0 0 18 18">
    <circle cx="9" cy="9" r="8.5" fill="#2a6fc4" stroke="#cfd8e3"/>
    <path d="M4.5 9h7M9 5.5 12.5 9 9 12.5" stroke="#fff" stroke-width="2" fill="none"/>
  </svg>
  <div class="avatar abs" role="img" aria-label="Portrait of the reviewer"></div>
  <svg class="abs" style="left:234px;top:52px" width="26" height="20" viewBox="0 0 26 20">
    <path d="M10 2C4 4 1 8 1 13a5 5 0 1 0 6-5C7 6 8 5 10 4ZM23 2C17 4 14 8 14 13a5 5 0 1 0 6-5C20 6 21 5 23 4Z" fill="#2f66ad"/>
  </svg>
  <p class="quote abs">Vis id minim dicant sensibus. Pri aliquip conclusionemque ad, ad malis evertitur<br>torquatos his. Has ei solum harum reprimique, id illum saperet tractatos his. Ei omnis<br>soleat antiopam quo. Ad augue inani postulant mel, mel ea qualisque forensibus.</p>
  <svg class="abs" style="left:630px;top:90px" width="26" height="20" viewBox="0 0 26 20">
    <path d="M3 18C9 16 12 12 12 7a5 5 0 1 0-6 5c0 2-1 3-3 4ZM16 18c6-2 9-6 9-11a5 5 0 1 0-6 5c0 2-1 3-3 4Z" fill="#2f66ad"/>
  </svg>
  <div class="author abs">Jane Doe</div>
</section>

<footer class="site-footer abs">
  <div class="footer-links abs">Terms of Service | Returns | Policy Privacy | Event | Contact | Blog | Sitemap</div>
  <div class="copyright abs">Copy Right © 2014. All rights reserved.</div>
  <svg class="abs" style="left:322px;top:54px" width="164" height="26" viewBox="0 0 164 26" aria-label="Social links">
    <g fill="#fff"><circle cx="14" cy="13" r="12"/><circle cx="41" cy="13" r="12"/><circle cx="68" cy="13" r="12"/><circle cx="95" cy="13" r="12"/><circle cx="123" cy="13" r="12"/><circle cx="150" cy="13" r="12"/></g>
  </svg>
  <div class="newsletter abs">News Letter</div>
  <svg class="abs" style="left:673px;top:61px" width="18" height="12" viewBox="0 0 18 12">
    <rect x="1" y="1" width="16" height="10" fill="none" stroke="#222" stroke-width="1.5"/>
    <path d="M1 1l8 6 8-6" fill="none" stroke="#222" stroke-width="1.5"/>
  </svg>
</footer>
</body>
</html>
```